Psychologist starting new business and needs a business card and possibly a logo to attract customer

I need a logo and business card for my new private practice as a Clinical Psychologist. The business will simply be called Maribel Ostrow Psychology". I'll be providing one on one therapy, mostly to male and female adult clients, and occasionally to children or adolescents. I'd like to see designs that include a small logo. I'd like it to have a professional feel to it. I'd like to convey a sense of warmth and caring. It could suggest the concept of two people working together towards a goal - but not necessarily. Colour wise, I'm not sure, except that I don't want it to have too much bright blue, which I think is a bit over-used in health logos. On the back I'd just like to see 3 or four lines to make appointments - each line would have one long line to write the date with a short line next to it on which to place the time.

```html
<!DOCTYPE html>
<html lang="en">
<head>
<meta charset="utf-8">
<title>Maribel Ostrow Psychology – Business Card</title>
<link rel="stylesheet" href="https://fonts.googleapis.com/css2?family=Poppins:wght@300;400;600&display=swap">
<style>
  :root {
    --lilac: #cdb6d9;
    --lilac-deep: #a98fc0;
    --line: #c9afd8;
    --paper: #ffffff;
    --backdrop: #ece8ee;
    --ink-light: #ffffff;
  }
  * { box-sizing: border-box; margin: 0; padding: 0; }
  html, body {
    width: 1200px; height: 1000px; overflow: hidden;
    background: var(--backdrop);
    font-family: "Poppins", "Helvetica Neue", Arial, sans-serif;
  }
  .canvas {
    position: relative; width: 1200px; height: 1000px;
  }
  .card {
    position: absolute; left: 210px;
    width: 780px; height: 440px;
    border-radius: 34px; overflow: hidden;
    background: var(--paper);
    box-shadow: 0 6px 22px rgba(60, 40, 70, 0.18);
  }
  .card--front { top: 40px; }
  .card--back { top: 520px; }

  /* Front */
  .front__top-band { position: absolute; left: 0; top: 0; width: 100%; height: 56px; background: var(--lilac); }
  .front__brand {
    position: absolute; left: 0; top: 56px; width: 100%; height: 176px;
    display: flex; align-items: center; justify-content: center; gap: 18px;
    color: var(--lilac-deep); font-weight: 300;
  }
  .brand__dot { width: 22px; height: 22px; border-radius: 50%; background: var(--lilac-deep); }
  .brand__text { text-align: center; line-height: 1; }
  .brand__name { font-size: 60px; letter-spacing: -1px; }
  .brand__field { font-size: 20px; letter-spacing: 14px; margin-top: 10px; padding-left: 14px; text-transform: uppercase; }
  .front__panel {
    position: absolute; left: 0; top: 232px; width: 100%; height: 208px;
    background: var(--lilac); color: var(--ink-light);
  }
  .contact {
    position: absolute; right: 40px; top: 26px;
    list-style: none; text-align: right; font-weight: 300; font-size: 22px; line-height: 34px;
  }
  .contact li { display: flex; justify-content: flex-end; align-items: center; gap: 8px; }
  .contact svg { width: 18px; height: 18px; }
  .holder { position: absolute; left: 44px; bottom: 34px; line-height: 1.15; }
  .holder__name { font-weight: 600; font-size: 30px; }
  .holder__role { font-weight: 300; font-size: 30px; }

  /* Back */
  .back__header {
    position: absolute; left: 0; top: 0; width: 100%; height: 118px;
    background: var(--lilac); color: var(--ink-light); font-weight: 300;
  }
  .back__title { position: absolute; left: 44px; top: 22px; font-size: 32px; }
  .back__col { position: absolute; bottom: 10px; font-size: 26px; }
  .back__col--time { right: 170px; }
  .back__col--date { right: 30px; }
  .rows { position: absolute; left: 40px; right: 30px; top: 150px; list-style: none; }
  .row { display: flex; align-items: flex-end; height: 68px; gap: 0; }
  .row__mark { width: 12px; height: 12px; border-radius: 50%; background: var(--lilac-deep); margin-right: 22px; margin-bottom: 2px; }
  .row__line { height: 3px; background: var(--line); }
  .row__line--name { width: 440px; margin-right: 40px; }
  .row__line--time { width: 100px; margin-right: 14px; }
  .row__line--date { width: 110px; }
</style>
</head>
<body>
<main class="canvas">
  <section class="card card--front" aria-label="Business card front">
    <div class="front__top-band"></div>
    <div class="front__brand">
      <span class="brand__dot"></span>
      <div class="brand__text">
        <div class="brand__name">Maribel Ostrow</div>
        <div class="brand__field">Psychology</div>
      </div>
    </div>
    <div class="front__panel">
      <ul class="contact">
        <li>123456789
          <svg viewBox="0 0 18 18" fill="none" stroke="#fff" stroke-width="1.5"><rect x="5" y="1.5" width="8" height="15" rx="1.5"/><line x1="8" y1="14" x2="10" y2="14"/></svg>
        </li>
        <li>123456789
          <svg viewBox="0 0 18 18" fill="none" stroke="#fff" stroke-width="1.5"><rect x="5" y="2" width="8" height="6"/><rect x="2" y="8" width="14" height="8" rx="1"/><line x1="5" y1="12" x2="13" y2="12"/></svg>
        </li>
        <li>hello@maribelostrow.com
          <svg viewBox="0 0 18 18" fill="none" stroke="#fff" stroke-width="1.5"><rect x="1.5" y="4" width="15" height="10"/><polyline points="1.5,4 9,10 16.5,4"/></svg>
        </li>
      </ul>
      <div class="holder">
        <div class="holder__name">Maribel Ostrow</div>
        <div class="holder__role">Psychologist</div>
      </div>
    </div>
  </section>

  <section class="card card--back" aria-label="Business card back">
    <header class="back__header">
      <h2 class="back__title" style="font-weight:300">Aappointments</h2>
      <span class="back__col back__col--time">Time</span>
      <span class="back__col back__col--date">Date</span>
    </header>
    <ul class="rows">
      <li class="row"><span class="row__mark"></span><span class="row__line row__line--name"></span><span class="row__line row__line--time"></span><span class="row__line row__line--date"></span></li>
      <li class="row"><span class="row__mark"></span><span class="row__line row__line--name"></span><span class="row__line row__line--time"></span><span class="row__line row__line--date"></span></li>
      <li class="row"><span class="row__mark"></span><span class="row__line row__line--name"></span><span class="row__line row__line--time"></span><span class="row__line row__line--date"></span></li>
      <li class="row"><span class="row__mark"></span><span class="row__line row__line--name"></span><span class="row__line row__line--time"></span><span class="row__line row__line--date"></span></li>
    </ul>
  </section>
</main>
</body>
</html>
```